I need new business cards designed

I would like to get some new designs on business cards. I will upload my logo for reference. The business cards that were designed for me a few months ago were too difficult for the print companies to work with. My company is Brushwillow.net LLC. It is an art company that sells painting and expression cards online.

```html
<!DOCTYPE html>
<html lang="en">
<head>
<meta charset="utf-8">
<title>Brushwillow.net LLC – Business Card</title>
<link href="https://fonts.googleapis.com/css2?family=Open+Sans:wght@400;600;700&display=swap" rel="stylesheet">
<style>
  :root {
    --stage: #2a2a2c;
    --card: #151515;
    --blue: #00a3df;
    --navy: #3b3d91;
    --orange: #f7941d;
    --green: #8dc63f;
    --white: #ffffff;
  }
  * { margin: 0; padding: 0; box-sizing: border-box; }
  html, body { width: 1200px; height: 900px; overflow: hidden; }
  body {
    background: var(--stage);
    font-family: "Open Sans", Arial, sans-serif;
    display: flex;
    align-items: center;
    justify-content: center;
    gap: 40px;
  }
  .card {
    position: relative;
    width: 550px;
    height: 314px;
    background: var(--card);
    border-radius: 18px;
    overflow: hidden;
  }
  .card-back { border: 3px solid var(--blue); }
  .waves { position: absolute; inset: 0; width: 100%; height: 100%; }
  .social { position: absolute; top: 34px; left: 22px; display: flex; gap: 6px; }
  .social span { width: 22px; height: 22px; background: var(--blue); display: block; }
  .brand { position: absolute; display: flex; align-items: center; gap: 10px; }
  .brand-mark { background: var(--orange); display: block; }
  .brand-name { color: var(--navy); font-weight: 400; white-space: nowrap; }
  .card-front .brand { left: 40px; top: 146px; }
  .card-front .brand-mark { width: 36px; height: 36px; }
  .card-front .brand-name { font-size: 22px; }
  .card-back .brand { left: 50%; top: 50%; transform: translate(-50%, -50%); gap: 16px; }
  .card-back .brand-mark { width: 64px; height: 64px; }
  .card-back .brand-name { font-size: 40px; }
  .divider { position: absolute; left: 286px; top: 62px; width: 1.5px; height: 140px; background: var(--blue); }
  .contact { position: absolute; left: 302px; top: 48px; color: var(--white); }
  .contact-name { color: var(--blue); font-weight: 700; font-size: 20px; letter-spacing: 0.5px; line-height: 1.2; }
  .contact-title { font-size: 11.5px; margin-bottom: 8px; }
  .contact-address { font-size: 11.5px; line-height: 1.45; margin-bottom: 6px; }
  .contact-list { list-style: none; font-size: 11.5px; line-height: 1.5; }
  .contact-list li { display: flex; align-items: center; gap: 7px; }
  .contact-list svg { width: 11px; height: 11px; fill: var(--blue); flex: none; }
</style>
</head>
<body>
  <section class="card card-front" aria-label="Card front">
    <svg class="waves" viewBox="0 0 550 314" preserveAspectRatio="none" aria-hidden="true">
      <path d="M0,268 C90,266 170,250 235,226 C180,256 90,276 0,279 Z" fill="var(--green)"/>
      <path d="M300,206 C380,166 470,160 550,158 L550,166 C470,168 385,178 305,210 Z" fill="var(--orange)"/>
      <path d="M0,288 C140,286 250,256 330,220 C410,184 480,176 550,174 L550,314 L0,314 Z" fill="var(--blue)"/>
    </svg>
    <div class="social" aria-label="Social links"><span></span><span></span><span></span></div>
    <div class="brand">
      <span class="brand-mark"></span>
      <span class="brand-name">Brushwillow.net</span>
    </div>
    <div class="divider"></div>
    <div class="contact">
      <p class="contact-name">OWEN HARTLEY</p>
      <p class="contact-title">Managing Director</p>
      <p class="contact-address">Your address, City<br>State, Zip 1234</p>
      <ul class="contact-list">
        <li><svg viewBox="0 0 24 24"><path d="M6.6 10.8a15 15 0 0 0 6.6 6.6l2.2-2.2c.3-.3.7-.4 1-.2 1.1.4 2.3.6 3.6.6.6 0 1 .4 1 1V20c0 .6-.4 1-1 1A17 17 0 0 1 3 4c0-.6.4-1 1-1h3.5c.6 0 1 .4 1 1 0 1.3.2 2.5.6 3.6.1.3 0 .7-.2 1z"/></svg>555-014-2290</li>
        <li><svg viewBox="0 0 24 24"><path d="M2 5h20v14H2z M2 5l10 8 10-8" /></svg>hello@brushwillow.net</li>
        <li><svg viewBox="0 0 24 24"><circle cx="12" cy="12" r="10"/></svg>www.Brushwillow.net</li>
      </ul>
    </div>
  </section>

  <section class="card card-back" aria-label="Card back">
    <div class="brand">
      <span class="brand-mark"></span>
      <span class="brand-name">Brushwillow.net</span>
    </div>
  </section>
</body>
</html>
```